Quick Start Android App Design Required!

We're designing an app to revolutionize data collection for outdoor works and road repairs. The app is currently being developed on Android and is due for launch later this year. We've created some functional wireframes that show how the app is to behave. We need you to make them look amazing!

Our intended audience is non-technical, and we'll need the app to be easy to navigate. We need a clean interface that is consistent with the Android interface. We expect you to use common Android design components and we're open to using the new Android Material design language.

We've included a set of wireframes that should show you what we're thinking, there are 12 screens that we need designed. We need your input on colors, fonts, layouts, and borders. If you use images, we'd prefer to see them only on the landing page.

To make things even easier, we have included designs for our website to show you what kind of design we like. Obviously we'd like to keep a consistent theme between the app and the website. We've included a copy of the logo for you to use where necessary too. Take note that we retain copyright to all materials included with this request.
Updates

Project Deadline Extended
Reason: We have decided to extend the deadline. There has been some late interest shown in the project and we'd like to give these designers the opportunity to refine their submissions.

Target Market(s)

Outdoor workers.

Industry/Entity Type

Android

Font styles to use
Serif
Sans Serif

Colors
3176b5

Requirements
Must have
• See the brief, all pages, designed as per brief.
Nice to have
• N/A
Should not have
• Too many images, please keep the design clean and simple.

```html
<!DOCTYPE html>
<html lang="en">
<head>
<meta charset="utf-8">
<title>Kerbtally – Quantities and Navigation</title>
<link href="https://fonts.googleapis.com/css2?family=Roboto:wght@400;500;700&display=swap" rel="stylesheet">
<style>
  :root {
    --canvas: #ebebeb;
    --status: #00528f;
    --primary: #0068b3;
    --accent: #1a73c4;
    --surface: #2e2e30;
    --surface-raised: #262628;
    --surface-deep: #141414;
    --divider: #1c1c1d;
    --text: #ffffff;
    --text-muted: #b4b4b6;
    --text-dim: #9a9a9c;
    --line: #6a6a6c;
    --icon: #8a8a8c;
    --success: #3cc15a;
    --danger: #e03a3a;
    --scrim-bar: #0b2b48;
    --map: #6e6e6c;
  }
  * { box-sizing: border-box; margin: 0; padding: 0; }
  html, body { width: 1200px; height: 1000px; overflow: hidden; }
  body { background: var(--canvas); font-family: "Roboto", Arial, sans-serif; position: relative; }

  .screen { position: absolute; top: 72px; width: 486px; height: 864px; background: var(--surface); overflow: hidden; }
  .screen--quantities { left: 98px; }
  .screen--menu { left: 610px; }
  .status-bar { position: absolute; left: 0; top: 0; width: 100%; height: 32px; background: var(--status); }

  .app-bar { position: absolute; left: 0; top: 32px; width: 100%; height: 76px; background: var(--primary); }
  .app-bar__title { position: absolute; left: 37px; top: 24px; color: var(--text); font-size: 27px; font-weight: 500; }

  .item-card { position: absolute; left: 0; width: 100%; }
  .item-card__label { position: absolute; left: 37px; top: 0; font-size: 16px; color: var(--text-muted); }
  .item-card__name { position: absolute; left: 36px; top: 22px; font-size: 32px; color: var(--text); }
  .field { position: absolute; border-bottom: 1px solid var(--line); color: var(--text-muted); font-size: 21.5px; padding-top: 2px; }
  .field--large { font-size: 32px; color: var(--text-dim); padding-top: 0; }
  .field__caret { position: absolute; right: 14px; top: 11px; width: 0; height: 0;
    border-left: 6px solid transparent; border-right: 6px solid transparent; border-top: 6px solid var(--text-muted); }
  .item-card__unit { position: absolute; left: 257px; font-size: 32px; color: var(--text); }
  .card-divider { position: absolute; left: 0; width: 100%; background: var(--divider); }

  .nav-bar { position: absolute; left: 0; bottom: 0; width: 100%; height: 86px; background: var(--surface-deep); }
  .nav-bar__btn { position: absolute; top: 30px; font-size: 21px; font-weight: 700; letter-spacing: .3px; display: flex; align-items: center; gap: 36px; }
  .nav-bar__btn--back { left: 33px; color: var(--icon); }
  .nav-bar__btn--next { right: 34px; color: var(--accent); gap: 32px; }

  .map-backdrop { position: absolute; left: 369px; top: 108px; width: 117px; height: 756px; background: var(--map); }
  .scrim-bar { position: absolute; left: 369px; top: 32px; width: 117px; height: 76px; background: var(--scrim-bar); }
  .close-icon { position: absolute; left: 432px; top: 62px; }

  .drawer { position: absolute; left: 0; top: 32px; width: 369px; height: 832px; background: var(--surface); }
  .drawer__brand { height: 118px; background: var(--surface-deep); display: flex; align-items: center; gap: 14px; padding-left: 42px; padding-top: 6px; }
  .drawer__brand-mark { width: 22px; height: 22px; background: var(--accent); }
  .drawer__brand-name { color: var(--text); font-size: 34px; font-weight: 700; letter-spacing: .5px; }
  .drawer__item { position: relative; height: 64.5px; display: flex; align-items: center; }
  .drawer__item--active { height: 66px; background: var(--surface-raised); }
  .drawer__icon { position: absolute; left: 24px; top: 50%; transform: translateY(-50%); width: 30px; height: 30px; }
  .drawer__label { position: absolute; left: 96px; color: var(--text); font-size: 21.5px; font-weight: 500; transform: translateY(1.5px); }
  .drawer__item--active .drawer__label { color: var(--accent); font-weight: 700; font-size: 21px; }
  .drawer__status { position: absolute; left: 280px; top: 50%; transform: translateY(-50%); }
  .drawer__count { color: var(--icon); font-size: 20px; font-weight: 700; left: 285px; }
</style>
</head>
<body>

<section class="screen screen--quantities">
  <div class="status-bar"></div>
  <header class="app-bar"><h1 class="app-bar__title">Quantities</h1></header>

  <div class="item-card" style="top:137px">
    <p class="item-card__label">Item Selected</p>
    <p class="item-card__name">Mowing</p>
    <div class="field field--large" style="left:36px;top:68px;width:193px;height:44px">Quantities</div>
    <div class="item-card__unit" style="top:68px">Unit</div>
    <div class="field" style="left:36px;top:130px;width:412px;height:36px">Asset Descriptions<span class="field__caret"></span></div>
    <div class="field" style="left:36px;top:195px;width:193px;height:36px">Asset<span class="field__caret"></span></div>
    <div class="field" style="left:256px;top:195px;width:195px;height:36px">Job<span class="field__caret"></span></div>
  </div>
  <div class="card-divider" style="top:421px;height:3px"></div>

  <div class="item-card" style="top:451px">
    <p class="item-card__label">Item Selected</p>
    <p class="item-card__name">Fertilising</p>
    <div class="field field--large" style="left:36px;top:68px;width:193px;height:44px">Quantities</div>
    <div class="item-card__unit" style="top:68px">Unit</div>
    <div class="field" style="left:36px;top:130px;width:412px;height:36px">Asset Descriptions<span class="field__caret"></span></div>
    <div class="field" style="left:36px;top:195px;width:193px;height:36px">Asset<span class="field__caret"></span></div>
    <div class="field" style="left:256px;top:195px;width:195px;height:36px">Job<span class="field__caret"></span></div>
  </div>
  <div class="card-divider" style="top:734px;height:10px"></div>

  <nav class="nav-bar">
    <span class="nav-bar__btn nav-bar__btn--back">
      <svg width="10" height="16" viewBox="0 0 10 16"><path d="M8 2 L2 8 L8 14" fill="none" stroke="currentColor" stroke-width="2"/></svg>BACK</span>
    <span class="nav-bar__btn nav-bar__btn--next">NEXT
      <svg width="10" height="16" viewBox="0 0 10 16"><path d="M2 2 L8 8 L2 14" fill="none" stroke="#8a8a8c" stroke-width="2"/></svg></span>
  </nav>
</section>

<section class="screen screen--menu">
  <div class="status-bar"></div>
  <div class="scrim-bar"></div>
  <svg class="close-icon" width="20" height="20" viewBox="0 0 22 22"><path d="M2 2 L20 20 M20 2 L2 20" stroke="#5a6470" stroke-width="2.5"/></svg>
  <div class="map-backdrop" role="img" aria-label="Dimmed street map of the work site behind the menu"></div>

  <aside class="drawer">
    <div class="drawer__brand"><span class="drawer__brand-mark"></span><span class="drawer__brand-name">KERBTALLY</span></div>

    <div class="drawer__item drawer__item--active">
      <svg class="drawer__icon" viewBox="0 0 30 30"><path d="M4 14 L15 5 L26 14 M7 12 V25 H23 V12" fill="none" stroke="#1a73c4" stroke-width="2.5"/></svg>
      <span class="drawer__label">Home</span>
    </div>
    <div class="drawer__item">
      <svg class="drawer__icon" viewBox="0 0 30 30"><circle cx="15" cy="15" r="10" fill="none" stroke="#8a8a8c" stroke-width="2"/><circle cx="15" cy="15" r="6" fill="#8a8a8c"/><path d="M15 1 V5 M15 25 V29 M1 15 H5 M25 15 H29" stroke="#8a8a8c" stroke-width="2"/></svg>
      <span class="drawer__label">Locations</span>
      <svg class="drawer__status" width="26" height="20" viewBox="0 0 26 20"><path d="M2 10 L9 17 L24 2" fill="none" stroke="#3cc15a" stroke-width="3"/></svg>
    </div>
    <div class="drawer__item">
      <svg class="drawer__icon" viewBox="0 0 30 30"><path d="M2 7 L4 9 L7 5 M2 14 L4 16 L7 12 M2 21 L4 23 L7 19" fill="none" stroke="#8a8a8c" stroke-width="1.5"/><path d="M11 7 H28 M11 14 H28 M11 21 H28" stroke="#8a8a8c" stroke-width="3"/></svg>
      <span class="drawer__label">Selections</span>
      <svg class="drawer__status" width="26" height="20" viewBox="0 0 26 20"><path d="M2 10 L9 17 L24 2" fill="none" stroke="#3cc15a" stroke-width="3"/></svg>
    </div>
    <div class="drawer__item">
      <svg class="drawer__icon" viewBox="0 0 30 30"><rect x="3" y="5" width="24" height="20" fill="none" stroke="#8a8a8c" stroke-width="2"/><path d="M6 22 L12 14 L17 19 L20 16 L24 22 Z" fill="#8a8a8c"/><circle cx="20" cy="10" r="2" fill="#8a8a8c"/></svg>
      <span class="drawer__label">Photos</span>
      <span class="drawer__label drawer__count">9</span>
    </div>
    <div class="drawer__item">
      <svg class="drawer__icon" viewBox="0 0 30 30"><rect x="5" y="2" width="20" height="26" fill="none" stroke="#8a8a8c" stroke-width="2"/><rect x="8" y="5" width="14" height="5" fill="#8a8a8c"/><path d="M8 13 H22 M8 17 H22 M8 21 H22 M8 25 H22 M11.5 12 V26 M15 12 V26 M18.5 12 V26" stroke="#8a8a8c" stroke-width="1.5"/></svg>
      <span class="drawer__label">Quantities</span>
      <svg class="drawer__status" width="24" height="24" viewBox="0 0 24 24"><path d="M2 2 L22 22 M22 2 L2 22" stroke="#e03a3a" stroke-width="2.5"/></svg>
    </div>
    <div class="drawer__item">
      <svg class="drawer__icon" viewBox="0 0 30 30"><path d="M6 2 H18 L25 9 V28 H6 Z" fill="#8a8a8c"/><path d="M18 2 V9 H25" fill="#6a6a6c"/></svg>
      <span class="drawer__label">Summary</span>
    </div>
  </aside>
</section>

</body>
</html>
```